New Business Card for Auto Repair and Performance Shop!

Need a redesign on a card that we have used for a while now. Something more update and modern, Serious but not too serious. Something confident, that shows the client that we are bespoke. Adding value.

Target Market(s)

Foreign Auto Repair and Performance

Industry/Entity Type

Automotive

Contact Information for Business Card

Utilize Logo, would like to change car silhouette to something Veltra,

Font styles to use
Sans Serif

Requirements
Must have
• business name, address, website, phone number.
MotoSerenix
4918 W. Birchwell Rd
Ashford, T.X. 70123
1-555-487-3106
www.moto-serenix-example.com

Specializing in Asian, European, and Domestic Auto Repair, Performance and Fabrication.

Clear space on back to for space to write appointment time and which client advisor helped the client.
Nice to have
• Up to the designers,

```html
<!DOCTYPE html>
<html lang="en">
<head>
<meta charset="utf-8">
<title>MotoSerenix Business Card</title>
<link rel="stylesheet" href="https://fonts.googleapis.com/css2?family=Roboto:wght@400;500;700&display=swap">
<style>
  :root {
    --page: #ffffff;
    --card-dark: #332e2f;
    --card-light: #ffffff;
    --accent: #ec1c24;
    --ink: #58585a;
    --ink-soft: #6b6b6d;
    --rule: #b8b8b8;
    --icon: #e8696e;
    --on-dark: #ffffff;
  }
  * { margin: 0; padding: 0; box-sizing: border-box; }
  html, body {
    width: 1200px; height: 1141px; overflow: hidden;
    background: var(--page);
    font-family: "Roboto", Arial, sans-serif;
  }
  .canvas { position: relative; width: 1200px; height: 1141px; }

  .card {
    position: absolute; left: 237px; width: 688px; height: 404px;
    border-radius: 11px; overflow: hidden;
    box-shadow: 0 10px 40px rgba(0,0,0,0.16);
  }
  .card--front { top: 125px; background: var(--card-dark); }
  .card--back { top: 599px; background: var(--card-light); }

  .edge-bar { position: absolute; background: var(--accent); }
  .edge-bar--top { left: 156px; top: 0; width: 369px; height: 7px; border-radius: 0 0 4px 4px; }
  .edge-bar--bottom { left: 156px; bottom: 0; width: 369px; height: 7px; border-radius: 4px 4px 0 0; }
  .edge-bar--side { right: 0; top: 138px; width: 11px; height: 172px; border-radius: 6px 0 0 6px; }

  .brand {
    position: absolute; display: flex; align-items: center; gap: 12px;
    font-weight: 700; letter-spacing: 0.5px; white-space: nowrap;
  }
  .brand__mark { width: 0.9em; height: 0.9em; background: var(--accent); border-radius: 3px; flex: none; }
  .card--front .brand {
    left: 0; right: 0; top: 190px; justify-content: center;
    font-size: 44px; line-height: 1; color: var(--on-dark);
  }
  .tagline {
    position: absolute; left: 0; right: 0; top: 266px;
    text-align: center; font-size: 16px; color: var(--on-dark);
  }
  .card--back .brand {
    right: 54px; top: 62px; font-size: 32px; line-height: 1; color: var(--card-dark);
  }

  .person { position: absolute; left: 43px; top: 168px; }
  .person__name { font-size: 24px; line-height: 1.2; font-weight: 700; color: var(--ink); }
  .person__role { font-size: 16px; color: var(--ink-soft); margin-top: 4px; }
  .person__rule {
    position: relative; width: 299px; height: 2px; margin-top: 10px;
    background: var(--rule);
  }
  .person__rule::before {
    content: ""; position: absolute; left: 0; top: 0; width: 137px; height: 2px;
    background: var(--icon);
  }

  .contacts { position: absolute; left: 43px; top: 250px; list-style: none; }
  .contacts li {
    display: flex; align-items: center; height: 33px;
    font-size: 16px; color: var(--ink-soft); white-space: nowrap;
  }
  .contacts svg { width: 18px; height: 18px; margin-right: 11px; fill: var(--icon); flex: none; }
</style>
</head>
<body>
<main class="canvas">

  <section class="card card--front" aria-label="Card front">
    <span class="edge-bar edge-bar--top"></span>
    <div class="brand"><span class="brand__mark"></span>MotoSerenix</div>
    <p class="tagline">Auto Repair and Performance Shop</p>
    <span class="edge-bar edge-bar--bottom"></span>
  </section>

  <section class="card card--back" aria-label="Card back">
    <div class="brand"><span class="brand__mark"></span>MotoSerenix</div>
    <span class="edge-bar edge-bar--side"></span>

    <div class="person">
      <h1 class="person__name">YOR NAME HERE</h1>
      <p class="person__role">Designation</p>
      <div class="person__rule"></div>
    </div>

    <ul class="contacts">
      <li>
        <svg viewBox="0 0 24 24" aria-hidden="true"><path d="M6.6 10.8a15.1 15.1 0 0 0 6.6 6.6l2.2-2.2c.3-.3.7-.4 1-.2 1.1.4 2.3.6 3.6.6.6 0 1 .4 1 1V20c0 .6-.4 1-1 1A17 17 0 0 1 3 4c0-.6.4-1 1-1h3.5c.6 0 1 .4 1 1 0 1.2.2 2.4.6 3.6.1.3 0 .7-.2 1z"/></svg>
        1-555-487-3106
      </li>
      <li>
        <svg viewBox="0 0 24 24" aria-hidden="true"><path d="M3 5h18v14H3z M4 6.5v.6l8 5 8-5v-.6z" fill-rule="evenodd"/></svg>
        name@moto-serenix-example.com
      </li>
      <li>
        <svg viewBox="0 0 24 24" aria-hidden="true"><path d="M12 2a10 10 0 1 0 0 20 10 10 0 0 0 0-20zm-1 17.9A8 8 0 0 1 4.2 10.4L9 15v1a2 2 0 0 0 2 2zm6.9-2.5A2 2 0 0 0 16 16h-1v-3a1 1 0 0 0-1-1H8v-2h2a1 1 0 0 0 1-1V7h2a2 2 0 0 0 2-2v-.4a8 8 0 0 1 2.9 12.8z"/></svg>
        www.moto-serenix-example.com
      </li>
      <li>
        <svg viewBox="0 0 24 24" aria-hidden="true"><path d="M12 2a7 7 0 0 0-7 7c0 5.2 7 13 7 13s7-7.8 7-13a7 7 0 0 0-7-7zm0 9.5A2.5 2.5 0 1 1 12 6.5a2.5 2.5 0 0 1 0 5z"/></svg>
        4918 W. Birchwell Rd, Ashford, T.X. 70123
      </li>
    </ul>
  </section>

</main>
</body>
</html>
```